Please look at my website to get a better understanding of my business: www.mokeranu.com
This business is about Life Coaching for Families, couples, teenagers and individuals. I work more w parents of teenagers (as well as teenagers) but not so much with young kids.
The card should be fun, not too busy, with a sense of flow and playfulness. Warm colors, artistic style (can have a family sculpture, paining or a picture in it). Basic information about myself and my company

Reason: I extended my due date for next Tuesday, November 13th. Please summit new designs if you haven't done so, and for those who submitted, thank you so much for your time and effort. I will make a decision next Tues, and will contact you if I need to revise some items. Much thanks to you all! Tali

Families, parents, teenagers, couples, individuals.

Business

• Business name: Mokeranu Kinward Circle Life Coaching
My name: Tali Welbrook, KCLC
Description of my work: Tandem-Path life coach
Tel: 555-304-7129
Website: www.MoKeRaNu.com
• Family sculpture, abstract painting or a picture, or simply a nice background w/out a picture added.
• Corporate feeling, cold colors, corporate symbols. no Sunset, or picture of families on the beach.
Don't include bar-code (from uploaded file 1, it is only the designer to find out more about my website).

```html
<!DOCTYPE html>
<html lang="en">
<head>
<meta charset="utf-8">
<title>Mokeranu Kinward Circle Life Coaching</title>
<link rel="stylesheet" href="https://fonts.googleapis.com/css2?family=Arimo:wght@700&family=Open+Sans:wght@400;700&display=swap">
<style>
  :root {
    --ring-yellow: #ffd200;
    --brand-orange: #f7a100;
    --paper: #ffffff;
    --ink: #111111;
  }
  * { margin: 0; padding: 0; box-sizing: border-box; }
  html, body { width: 1200px; height: 667px; overflow: hidden; background: var(--paper); }
  .business-card {
    position: relative;
    width: 1200px;
    height: 667px;
    overflow: hidden;
    background: var(--paper);
  }
  .card-backdrop { position: absolute; inset: 0; }
  .brand {
    position: absolute;
    left: 40px;
    top: 73px;
    width: 705px;
    text-align: center;
    font-family: "Arimo", Arial, sans-serif;
    font-weight: 700;
    color: var(--brand-orange);
  }
  .brand-name {
    font-size: 136px;
    line-height: 1;
    font-weight: 700;
  }
  .brand-tagline {
    margin-top: 16px;
    font-size: 38px;
    line-height: 1;
    letter-spacing: 1px;
    white-space: nowrap;
  }
  .brand-rule {
    margin: 12px 0 0 45px;
    width: 617px;
    height: 3px;
    background: linear-gradient(90deg, rgba(247,161,0,0) 0%, var(--brand-orange) 20%, var(--brand-orange) 100%);
  }
  .contact-card {
    position: absolute;
    left: 790px;
    top: 96px;
    width: 560px;
    height: 456px;
    background: var(--paper);
    transform-origin: 0 0;
    transform: rotate(14deg);
    box-shadow: -6px 10px 10px rgba(0, 0, 0, 0.55);
    font-family: "Open Sans", Arial, sans-serif;
    color: var(--ink);
  }
  .contact-card p { position: absolute; white-space: nowrap; }
  .coach-name  { left: 28px;  top: 176px; font-size: 46px; line-height: 1.1; }
  .coach-role  { left: 95px;  top: 258px; font-size: 27px; line-height: 1.2; }
  .coach-phone { left: 121px; top: 334px; font-size: 24px; font-weight: 700; line-height: 1.2; }
  .coach-web   { left: 119px; top: 374px; font-size: 23px; line-height: 1.2; }
</style>
</head>
<body>
<div class="business-card">
  <svg class="card-backdrop" width="1200" height="667" viewBox="0 0 1200 667" aria-hidden="true">
    <defs>
      <linearGradient id="left-wash" x1="0" y1="0" x2="1" y2="0">
        <stop offset="0" stop-color="#f8edb0"/>
        <stop offset="0.55" stop-color="#fbf6dc"/>
        <stop offset="1" stop-color="#ffffff" stop-opacity="0"/>
      </linearGradient>
      <linearGradient id="lower-fade" x1="0" y1="0" x2="0" y2="1">
        <stop offset="0" stop-color="#ffffff" stop-opacity="0"/>
        <stop offset="1" stop-color="#ffffff" stop-opacity="0.9"/>
      </linearGradient>
      <linearGradient id="frame-fill" x1="0" y1="1" x2="0.6" y2="0.3">
        <stop offset="0" stop-color="#ff9d00"/>
        <stop offset="0.45" stop-color="#ffd000"/>
        <stop offset="1" stop-color="#ffe000"/>
      </linearGradient>
      <linearGradient id="big-ring" x1="0" y1="1" x2="1" y2="0">
        <stop offset="0" stop-color="#ff9a00"/>
        <stop offset="1" stop-color="#ffd000"/>
      </linearGradient>
    </defs>
    <rect x="0" y="0" width="800" height="667" fill="url(#left-wash)"/>
    <rect x="0" y="300" width="800" height="367" fill="url(#lower-fade)"/>
    <circle cx="865" cy="10" r="88" fill="none" stroke="var(--ring-yellow)" stroke-width="6"/>
    <circle cx="330" cy="640" r="300" fill="none" stroke="url(#big-ring)" stroke-width="44"/>
    <circle cx="680" cy="690" r="185" fill="none" stroke="var(--ring-yellow)" stroke-width="20"/>
    <path fill="url(#frame-fill)" fill-rule="evenodd"
          d="M0 0H1200V667H0Z M20 20V647H1180V20Z"/>
  </svg>

  <div class="brand">
    <h1 class="brand-name">Mokeranu</h1>
    <p class="brand-tagline">Kinward Circle Life Coaching</p>
    <div class="brand-rule"></div>
  </div>

  <div class="contact-card">
    <p class="coach-name">Tali Welbrook, KCLC</p>
    <p class="coach-role">Tandem-Path life coach</p>
    <p class="coach-phone">Ph. 555-304-7129</p>
    <p class="coach-web">www.MoKeRaNu.com</p>
  </div>
</div>
</body>
</html>
```